UPliften website redesign to provide information about experiential workshops, film work and other

We need a redesign of our website upliften.org. We conduct experiential workshops of discovery and transformation for individuals and organizations. We need the website to reflect the full extent of UPliften programs, and be an information hub for UPliften workshops and communities as they develop.

The attached documents contain information about the organization - it's brandbook, copy for web pages, a website layout and a couple of images.

The site is for individuals and companies looking to promote and be change to make a difference. It should be warm, welcoming, and create excitement around the concepts and the ability to discover a new way of being in the world. We are about creating communities around the globe who will embody play, freedom, curiosity and expanded possibilities. We are creating a space for this to happen, both physically (workshops) and online.

We will be on either a BrightPanel, but mos tlikely a Zantro plaform.

Please look at the current site at www.upliften.org

Target Market(s)

Initially, are target market will be baby boomers, but will expand to include millennials and students.

Coding

Coded - Design and coding required

Number of Pages Required

5+ page

Requirements
Must have
• The colors, logo and fonts from the brand book.
Nice to have
• Complimentary use of brand colors to create an attractive presentation and energy

```html
<!DOCTYPE html>
<html lang="en">
<head>
<meta charset="utf-8">
<title>UPliften — Experiential Workshops</title>
<link href="https://fonts.googleapis.com/css2?family=League+Spartan:wght@300;400;500;600;700&family=Questrial&display=swap" rel="stylesheet">
<style>
:root{
  --orange:#f47b3b;
  --orange-light:#f5b152;
  --orange-mid:#f59a43;
  --ink:#1c1c1c;
  --text:#6f6f6f;
  --muted:#a8a8a8;
  --line:#e4e4e4;
  --white:#ffffff;
  --tint:#fafafa;
}
*{box-sizing:border-box;margin:0;padding:0}
html,body{width:1200px;height:2550px;overflow:hidden;background:var(--white)}
body{position:relative;font-family:"Questrial",sans-serif;color:var(--text)}
.abs{position:absolute}
h1,h2,h3,h4,.brand,.feature-label,.card-label{font-family:"League Spartan",sans-serif}

/* Hero */
.hero{left:0;top:0;width:1200px;height:595px;overflow:hidden}
.hero-left{left:0;top:0;width:600px;height:595px;background:linear-gradient(180deg,#8a8a8a 0%,#a3a3a3 60%,#b2b2b2 100%)}
.hero-right{left:600px;top:0;width:600px;height:595px;background:linear-gradient(135deg,#4a4a4a 0%,#262626 45%,#141414 100%)}
.hero-photo{left:820px;top:210px;width:380px;height:385px;background:radial-gradient(ellipse at 60% 60%,#3d3a3a 0%,#262424 55%,rgba(20,20,20,0) 80%)}
.brand{left:162px;top:54px;color:var(--white);font-size:31px;font-weight:700;letter-spacing:2px}
.menu-btn{left:995px;top:44px;width:42px;height:34px;background:#4a4a4a;display:flex;flex-direction:column;justify-content:center;align-items:center;gap:4px}
.menu-btn span{display:block;width:16px;height:2px;background:var(--white)}
.hero-vertical{left:505px;top:8px;height:560px;writing-mode:vertical-rl;transform:rotate(180deg);color:var(--white);font-family:"League Spartan",sans-serif;font-weight:300;font-size:100px;letter-spacing:4px;text-align:left;line-height:1}
.hero-question{font-family:"League Spartan",sans-serif;font-weight:500;font-size:31px;line-height:42px;color:var(--orange-mid);text-transform:uppercase}
.q-left{left:162px;top:256px}
.q-right{left:650px;top:256px}
.q-underline{left:832px;top:362px}

/* Feature band */
.feature-band{left:0;top:595px;width:750px;height:120px;background:linear-gradient(90deg,var(--orange-light) 0%,var(--orange-mid) 55%,var(--orange) 100%);display:flex;align-items:center;padding-left:30px;gap:30px}
.feature{display:flex;align-items:center;gap:10px}
.feature-icon{width:22px;height:22px;border:2px solid var(--white);flex:none}
.feature-label{color:var(--white);font-size:12px;font-weight:600;text-transform:uppercase;line-height:13px}
.band-note{left:779px;top:631px}
.band-note .rule{width:28px;height:3px;background:var(--orange);margin-bottom:18px}
.band-note p{font-family:"League Spartan",sans-serif;font-weight:500;font-size:16px;line-height:26px;color:var(--ink);width:275px}

/* Welcome */
.collage-a{left:340px;top:812px;width:131px;height:110px;border-radius:6px;background:linear-gradient(135deg,#b88c6a,#7a5b44)}
.collage-b{left:340px;top:903px;width:170px;height:188px;border-radius:6px;background:linear-gradient(160deg,#6f7467,#3f463f 60%,#8a8d86)}
.collage-c{left:162px;top:1000px;width:128px;height:114px;border-radius:6px;background:linear-gradient(160deg,#5d7a3c,#9a8a6a)}
.vision-card{left:162px;top:797px;width:180px;height:205px;background:var(--orange-light);padding:30px 24px}
.vision-card small{display:block;color:var(--white);font-size:10px;text-transform:uppercase;margin-bottom:8px}
.vision-card h3{color:var(--white);font-size:24px;font-weight:500;line-height:27px}
.welcome{left:598px;top:826px;width:445px}
.section-title{font-size:25px;font-weight:500;color:var(--ink);line-height:29px}
.body-copy{font-size:11.5px;line-height:19px;color:var(--text)}
.welcome .body-copy{margin-top:22px}
.welcome .body-copy + .body-copy{margin-top:16px}
.learn-more{display:flex;align-items:center;gap:6px;color:var(--orange);font-size:11px;font-weight:600;font-family:"League Spartan",sans-serif}
.welcome .learn-more{margin-top:22px}

/* What we do */
.what-we-do{left:162px;top:1213px;width:300px}
.what-we-do h2{font-size:25px;font-weight:500;color:var(--orange)}
.what-we-do h4{margin-top:18px;font-size:14px;font-weight:600;color:var(--ink)}
.what-we-do .body-copy{margin-top:10px}
.nav-arrows{left:162px;top:1440px;display:flex;gap:18px}
.arrow-btn{width:29px;height:29px;border-radius:50%;display:flex;align-items:center;justify-content:center}
.arrow-prev{border:1px solid #cfcfcf}
.arrow-next{background:var(--orange)}
.movements-title{left:488px;top:1226px;font-family:"League Spartan",sans-serif;font-weight:600;font-size:15px;color:var(--ink)}
.movements-title span{color:var(--orange)}
.movements-band{left:488px;top:1258px;width:712px;height:120px;background:linear-gradient(90deg,var(--orange-light),var(--orange-mid) 50%,var(--orange))}
.card{top:1278px;width:160px;height:167px;background:var(--white);box-shadow:0 8px 24px rgba(0,0,0,.08);border-radius:3px;display:flex;flex-direction:column;align-items:center;padding-top:30px}
.card-icon{height:60px;display:flex;align-items:center;justify-content:center}
.card-label{margin-top:20px;font-size:13px;font-weight:500;color:var(--ink);text-align:center;line-height:15px}

/* Workshop feature */
.peace-block{left:162px;top:1663px;width:210px;height:233px;background:linear-gradient(180deg,var(--orange-light),var(--orange-mid) 60%,var(--orange))}
.peace-frame{left:209px;top:1557px;width:260px;height:290px;background:var(--white);padding:10px;box-shadow:0 8px 24px rgba(0,0,0,.12)}
.peace-photo{width:100%;height:100%;background:linear-gradient(180deg,#4f6b3a 0%,#7c8b5d 45%,#c9bfae 75%,#a9a296 100%)}
.peace{left:522px;top:1584px;width:560px}
.mark-square{width:22px;height:22px;background:#dcdcdc}
.peace .mark-square{margin-top:16px}
.peace .body-copy{margin-top:24px}
.peace .body-copy + .body-copy{margin-top:14px}
.peace .learn-more{margin-top:26px}

/* Community */
.community{left:162px;top:1983px}
.community h3{font-size:16px;font-weight:600;color:var(--ink)}
.community .mark-square{margin-top:14px}
.community-text{left:341px;top:1986px;width:695px;font-size:11.5px;line-height:19px;color:var(--ink)}
.community-text a{color:var(--ink)}

/* Footer */
.footer-tint{left:620px;top:2130px;width:580px;height:420px;background:var(--tint)}
.contact-card{left:530px;top:2179px;width:456px;height:308px;background:var(--white);box-shadow:0 10px 30px rgba(0,0,0,.08);padding:42px 0 0 38px}
.contact-card h2{font-size:32px;font-weight:500;color:var(--ink);line-height:36px}
.contact-card h2 span{color:var(--orange)}
.contact-list{position:absolute;left:210px;top:44px;width:208px}
.contact-item{border-bottom:1px dashed var(--line);padding-bottom:16px;margin-bottom:20px}
.contact-item .label{font-size:9.5px;color:var(--ink);text-transform:uppercase}
.contact-item .value{font-size:12px;color:var(--ink);font-family:"League Spartan",sans-serif;font-weight:600}
.contact-item .value.email{font-size:19px;color:var(--orange);font-weight:500;margin-top:2px}
.contact-item .sub{font-size:8.5px;color:var(--muted);text-transform:uppercase;margin-top:2px}
.footer-col{top:2248px}
.footer-col h4{font-size:12px;color:var(--muted);font-weight:500;margin-bottom:20px}
.footer-col li{list-style:none;font-size:10px;color:var(--ink);margin-bottom:10px}
.social{left:162px;top:2404px}
.social h4{font-size:12px;color:var(--muted);font-weight:500;margin-bottom:18px}
.social-row{display:flex;gap:23px}
.social-dot{width:13px;height:13px;border-radius:50%;border:1.5px solid var(--ink)}
.copyright{left:162px;top:2510px;font-size:9px;color:var(--text)}
</style>
</head>
<body>

<section class="hero abs">
  <div class="hero-left abs"></div>
  <div class="hero-right abs"></div>
  <div class="hero-photo abs" role="img" aria-label="Hand in a suit sleeve holding a pen, writing on the dark background"></div>
  <div class="brand abs">UPLIFTEN</div>
  <div class="menu-btn abs"><span></span><span></span><span></span></div>
  <div class="hero-vertical abs">UPLIFTEN</div>
  <h1 class="hero-question q-left abs">What world<br>do we want<br>to live in?</h1>
  <h1 class="hero-question q-right abs">What kind of<br>life do you want<br>to create?</h1>
  <svg class="q-underline abs" width="115" height="12" viewBox="0 0 115 12"><path d="M2 9 Q55 3 113 5" stroke="#fff" stroke-width="3" fill="none" stroke-linecap="round"/></svg>
</section>

<div class="feature-band abs">
  <div class="feature"><span class="feature-icon"></span><span class="feature-label">Moves energy</span></div>
  <div class="feature"><span class="feature-icon"></span><span class="feature-label">Creates opportunities<br>for connecting</span></div>
  <div class="feature"><span class="feature-icon"></span><span class="feature-label">Supports conscious<br>evolution</span></div>
  <div class="feature"><span class="feature-icon"></span><span class="feature-label">Deepens experience<br>of life</span></div>
</div>
<div class="band-note abs">
  <div class="rule"></div>
  <p>Discover an Opportunity to Live a More Dynamic and Meaningful Life</p>
</div>

<div class="collage-a abs" role="img" aria-label="Workshop room with participants"></div>
<div class="collage-b abs" role="img" aria-label="Group performance in costume in a gallery"></div>
<div class="collage-c abs" role="img" aria-label="Participants seated in a circle by the windows"></div>
<div class="vision-card abs">
  <small>Vison</small>
  <h3>We envision a world in which all people…</h3>
</div>
<section class="welcome abs">
  <h2 class="section-title">Welcome To The<br>UPliften</h2>
  <p class="body-copy">We envision a world in which all people and communities can challenge and break free from stories that no longer serve us. We believe that solutions to contemporary challenges will emerge from a place of curiosity, love and connection.</p>
  <p class="body-copy">Through inspiration, conscious reflection, and collaboration, we take responsibility for the world we are manifesting, and we can discover and create new possibilities for the lives and the society we desire to build.</p>
  <div class="learn-more">Learn More
    <svg width="11" height="11" viewBox="0 0 11 11"><rect x="0.75" y="0.75" width="9.5" height="9.5" fill="none" stroke="#f47b3b" stroke-width="1.2"/><path d="M3 5.5h5M6 3.5l2 2-2 2" stroke="#f47b3b" stroke-width="1.2" fill="none"/></svg>
  </div>
</section>

<section class="what-we-do abs">
  <h2>What We Do</h2>
  <h4>UPliften Life:</h4>
  <p class="body-copy">UPliften Life is a workshop designed to re-engage you with life. Through interactive exercises and personal exploration, you are taken on a journey that ultimately leaves you experiencing life as a Creator. You will learn to see beliefs and patterns that hold you back in work and relationships as well as a path to transforming the story of your life.</p>
</section>
<div class="nav-arrows abs">
  <div class="arrow-btn arrow-prev"><svg width="12" height="8" viewBox="0 0 12 8"><path d="M11 4H1M4 1L1 4l3 3" stroke="#1c1c1c" stroke-width="1.3" fill="none"/></svg></div>
  <div class="arrow-btn arrow-next"><svg width="12" height="8" viewBox="0 0 12 8"><path d="M1 4h10M8 1l3 3-3 3" stroke="#fff" stroke-width="1.3" fill="none"/></svg></div>
</div>
<div class="movements-title abs">UPliften Life is a 2-3 day workshop experienced in <span>5 movements:</span></div>
<div class="movements-band abs"></div>
<div class="card abs" style="left:517px">
  <div class="card-icon"><svg width="56" height="56" viewBox="0 0 56 56"><circle cx="28" cy="28" r="26" fill="none" stroke="#f47b3b" stroke-width="2"/></svg></div>
  <div class="card-label">Curiosity</div>
</div>
<div class="card abs" style="left:699px">
  <div class="card-icon"><svg width="50" height="50" viewBox="0 0 50 50"><rect x="1" y="1" width="48" height="48" fill="none" stroke="#f47b3b" stroke-width="2"/></svg></div>
  <div class="card-label">Awareness</div>
</div>
<div class="card abs" style="left:879px">
  <div class="card-icon"><svg width="58" height="58" viewBox="0 0 58 58"><path d="M29 2L56 29 29 56 2 29Z" fill="none" stroke="#f47b3b" stroke-width="2"/></svg></div>
  <div class="card-label">Owning Your<br>Creation</div>
</div>

<div class="peace-block abs"></div>
<div class="peace-frame abs"><div class="peace-photo" role="img" aria-label="Two workshop leaders seated in conversation before large windows and trees"></div></div>
<section class="peace abs">
  <h2 class="section-title">Stirring the Calm</h2>
  <div class="mark-square"></div>
  <p class="body-copy">The Stirring the Calm workshop—an extension of the documentary of the same name—is an experiential process to transform participants into disturbers of the status quo within themselves, to enhance their relationships with others, and to change the environments in which they exist—and ultimately society—for the better.</p>
  <p class="body-copy">This workshop experience challenges us all to understand the narratives we live within, to look at our current roles in society, and to decide what role we will play to create a more humane, just and peaceful world, for all. It all starts with our willingness to disturb the “peace” of the status quo.</p>
  <div class="learn-more">Learn More
    <svg width="11" height="11" viewBox="0 0 11 11"><rect x="0.75" y="0.75" width="9.5" height="9.5" fill="none" stroke="#f47b3b" stroke-width="1.2"/><path d="M3 5.5h5M6 3.5l2 2-2 2" stroke="#f47b3b" stroke-width="1.2" fill="none"/></svg>
  </div>
</section>

<section class="community abs">
  <h3>In Your Community</h3>
  <div class="mark-square"></div>
</section>
<p class="community-text abs">Bring UPliften or the Stirring the Calm workshop to your community. We would love to hear from you. Please fill out the brief form here<br><a href="#">(link to In Your Community page)</a></p>

<footer>
  <div class="footer-tint abs"></div>
  <div class="footer-col abs" style="left:162px">
    <h4>About</h4>
    <ul><li>About</li><li>WorkShop</li><li>UPliften Project</li><li>Films</li><li>Store &amp; Resources</li></ul>
  </div>
  <div class="footer-col abs" style="left:338px">
    <h4>Company</h4>
    <ul><li>Community</li><li>Contact Us</li></ul>
  </div>
  <div class="social abs">
    <h4>Social Media</h4>
    <div class="social-row"><span class="social-dot"></span><span class="social-dot"></span><span class="social-dot"></span><span class="social-dot"></span></div>
  </div>
  <div class="contact-card abs">
    <h2>Contact<br>Us<span>.</span></h2>
    <div class="contact-list">
      <div class="contact-item"><div class="label">Need a solution?</div><div class="value email">hello@upliften.org</div></div>
      <div class="contact-item"><div class="value">Lorem Ipsum Dolor Sit Amet Consectetur</div><div class="sub">Head Office</div></div>
      <div class="contact-item"><div class="value">555.014.2760</div><div class="sub">Call Support</div></div>
    </div>
  </div>
  <p class="copyright abs">© Copyright 2018 UPliften, All Rights Reserved.</p>
</footer>

</body>
</html>
```